Custom PowerPoint Template for Training & Workshop Presentations

I am looking for a professional designer to create a custom PowerPoint template (PPTX) for my training and workshop materials. My trainings are designed for: HR professionals and Learning & Development specialists;
Executives and team leaders; Organizations investing in employee development and workplace learning; Participants in professional development workshops, seminars, and didactics trainings
The template should therefore appear trustworthy, calm, friendly, structured, and competence‑oriented. The design should be visually appealing, easy to read, and fully editable.

All branding files are attached to this project.
Please use them as the main reference for your design:
Logo (included as attachment)
Brand color specifications (included as attachment)
Font specifications related to the logo and brand (included as attachment)

What I need:
--> Title Slide: Title, subtitle, name, logo
(1–2 variations)
--> Agenda / Overview Slide
--> Content Slides
--> Text only
--> Text + image
-->Two-column
--> Section header
--> Quote / key message
--> Graphic / Model Slides: (1–2 layouts for frameworks, processes, models)
--> Tables & Charts: (Table styles in brand colors; Chart design aligned with typography and color palette)
--> Closing Slide: (Contact or call-to-action; Optional second variation)

All layouts must be built properly inside the PowerPoint Slide Master

```html
<!DOCTYPE html>
<html lang="en">
<head>
<meta charset="utf-8">
<title>Training Presentation Template – Slide Overview</title>
<link href="https://fonts.googleapis.com/css2?family=Archivo+Black&family=Roboto:wght@300;400;500;700&family=Roboto+Condensed:wght@300;400;700&display=swap" rel="stylesheet">
<style>
:root{
  --blue:#1f5b95;
  --blue-dark:#174a7c;
  --blue-soft:#8ea9c7;
  --blue-pale:#c9d6e5;
  --grey-pale:#e6ebf1;
  --ink:#111418;
  --text:#5b6470;
  --canvas:#eef0f3;
  --white:#ffffff;
}
*{box-sizing:border-box;margin:0;padding:0}
html,body{width:1200px;height:3028px;overflow:hidden}
body{background:var(--canvas);font-family:"Roboto",sans-serif;color:var(--ink);position:relative}
.slide{position:absolute;width:600px;height:338px;overflow:hidden;background:var(--white);box-shadow:0 1px 3px rgba(0,0,0,.12)}
.abs{position:absolute}
.photo{position:absolute;background:linear-gradient(135deg,#c9b7a4 0%,#8d9fb4 55%,#5f7895 100%)}
.photo.warm{background:linear-gradient(135deg,#d8b48c 0%,#a88466 50%,#6d7f96 100%)}
.photo.cool{background:linear-gradient(135deg,#dfe4ea 0%,#a9b7c7 50%,#6f869f 100%)}
.h-display{font-family:"Archivo Black",sans-serif;font-weight:400;line-height:1.15;letter-spacing:.2px}
.h-display .accent{color:var(--blue)}
.sub{font-family:"Roboto Condensed",sans-serif;font-weight:300}
.body-xs{font-size:6px;line-height:10px;color:var(--text)}
.white{color:var(--white)}
.pageno{position:absolute;right:30px;bottom:20px;font-size:6px;font-weight:700;color:var(--blue)}
.brand{position:absolute;display:flex;align-items:center;gap:5px;font-family:"Roboto",sans-serif;font-weight:500;color:var(--blue);white-space:nowrap;letter-spacing:.3px}
.brand .mark{display:inline-block;width:6px;height:6px;border-radius:50%;background:currentColor}
.brand-sm{top:14px;right:28px;font-size:7px}
.brand-sm .mark{width:5px;height:5px}
.brand-lg{font-size:14px}
.brand-lg .mark{width:10px;height:10px}
.brand.light{color:var(--white)}
.name{font-family:"Roboto Condensed",sans-serif;font-weight:700;font-size:11px;color:var(--ink)}
.badge{position:absolute;background:var(--blue);color:var(--white);font-family:"Roboto Condensed",sans-serif;font-size:8.5px;padding:2px 0;width:172px;text-align:center}
.toc-row{position:absolute;left:190px;width:410px;height:60px;display:flex;align-items:center;border-bottom:1px solid rgba(255,255,255,.25)}
.toc-label{width:45px;font-size:8px;color:var(--white);padding-left:10px}
.toc-num{width:86px;font-family:"Archivo Black",sans-serif;font-size:26px;color:var(--white)}
.toc-text{width:200px;font-size:5.6px;line-height:9px;color:rgba(255,255,255,.8)}
.step-label{position:absolute;width:80px;text-align:center;font-family:"Archivo Black",sans-serif;font-size:10px}
.step-dot{position:absolute;width:6px;height:6px;border-radius:50%;background:var(--blue)}
.card-blue{position:absolute;background:var(--blue);color:var(--white);padding:10px 12px}
.card-title{font-family:"Archivo Black",sans-serif;font-size:7px;margin-top:6px;line-height:1.2}
.card-text{font-size:5.6px;line-height:9px;color:rgba(255,255,255,.8);margin-top:4px}
.icon-box{width:22px;height:22px}
</style>
</head>
<body>

<section class="slide title-slide-a" style="left:0;top:20px">
  <div class="abs" style="left:0;top:0;width:417px;height:187px;background:var(--blue)"></div>
  <div class="photo cool" role="img" aria-label="Portrait photo of the trainer" style="left:417px;top:0;width:183px;height:187px"></div>
  <h1 class="abs h-display white" style="left:30px;top:30px;font-size:33px">Business Training<br>Title Goes Here</h1>
  <p class="abs sub white" style="left:30px;top:138px;font-size:21px">Subtitle Here</p>
  <p class="abs name" style="left:30px;top:257px">Dr. phil. Lena Hartwig, MBA</p>
  <div class="badge" style="left:30px;top:275px">Expertin für Didaktik und Selbstführung</div>
  <div class="brand brand-lg" style="left:395px;top:262px"><span class="mark"></span>Hartwig Akademie</div>
</section>

<section class="slide title-slide-b" style="left:600px;top:20px;background:var(--blue)">
  <div class="brand brand-sm light"><span class="mark"></span>Hartwig Akademie</div>
  <h1 class="abs h-display white" style="left:30px;top:50px;font-size:33px">Business Training<br>Title Goes Here</h1>
  <p class="abs sub white" style="left:30px;top:155px;font-size:21px">Subtitle Here</p>
  <div class="abs" style="left:384px;top:56px;width:192px;height:135px;background:var(--white)"></div>
  <div class="photo warm" role="img" aria-label="Photo of a smiling team working together at a table" style="left:28px;top:191px;width:356px;height:147px"></div>
  <div class="abs" style="left:384px;top:191px;width:192px;height:27px;background:var(--blue-soft);font-size:6px;color:var(--white);padding:10px 0 0 20px">Read more &nbsp;&nbsp;&nbsp;&nbsp;&nbsp;&nbsp;&nbsp;&nbsp;&nbsp;&nbsp;&nbsp;&nbsp;&nbsp;&nbsp;&nbsp;&nbsp;&nbsp;&nbsp;&nbsp;&nbsp;&nbsp;↗</div>
</section>

<section class="slide agenda" style="left:0;top:398px;background:var(--blue)">
  <div class="photo warm" role="img" aria-label="Photo of a woman with a laptop sitting on wooden stairs" style="left:0;top:0;width:148px;height:338px"></div>
  <h2 class="abs h-display white" style="left:195px;top:44px;font-size:22px">Table of Content</h2>
  <div class="toc-row" style="top:90px"><span class="toc-label">Page</span><span class="toc-num">01.</span><span class="toc-text">Opening of the workshop, goals for the day, short round of introductions and a first look at the agenda.</span></div>
  <div class="toc-row" style="top:150px"><span class="toc-label">Page</span><span class="toc-num">02.</span><span class="toc-text">Core concepts and models, with short examples from daily work and room for questions from the group.</span></div>
  <div class="toc-row" style="top:210px"><span class="toc-label">Page</span><span class="toc-num">03.</span><span class="toc-text">Practice in small teams, case work and shared reflection on what can be used right away at work.</span></div>
  <div class="toc-row" style="top:270px;border-bottom:none"><span class="toc-label">Page</span><span class="toc-num">04.</span><span class="toc-text">Summary of key learnings, next steps, feedback round and a clear plan for the transfer into practice.</span></div>
</section>

<section class="slide section-header" style="left:600px;top:398px">
  <div class="brand brand-sm"><span class="mark"></span>Hartwig Akademie</div>
  <div class="abs" style="left:0;top:119px;width:158px;height:219px;background:var(--blue)"></div>
  <div class="photo" role="img" aria-label="Photo of two colleagues smiling in a bright office" style="left:46px;top:0;width:215px;height:297px"></div>
  <div class="abs" style="left:58px;top:193px;width:189px;height:88px;background:rgba(142,169,199,.9);padding:14px 16px">
    <svg width="16" height="12" viewBox="0 0 16 12" fill="none" stroke="#fff" stroke-width="1.3"><circle cx="6" cy="3.5" r="2.5"/><path d="M1 11c0-3 2.2-4.5 5-4.5s5 1.5 5 4.5"/><path d="M11 1.5a2.3 2.3 0 010 4.2M13 7c1.3.6 2 1.8 2 4"/></svg>
    <p style="font-size:5.6px;line-height:9px;color:rgba(255,255,255,.9);margin-top:8px">Short key message for this section, placed over the photo in two lines.</p>
  </div>
  <h2 class="abs h-display" style="left:304px;top:92px;font-size:21px;line-height:1.2">Developing Agile,<br><span class="accent">High-Performing</span><br><span class="accent">Teams</span></h2>
  <p class="abs body-xs" style="left:304px;top:185px;width:240px">This section looks at how teams learn, adapt and grow over time. It shows the habits that help people share knowledge, give clear feedback and take on shared responsibility for results in a changing work setting.</p>
  <span class="pageno">4</span>
</section>

<section class="slide text-image" style="left:0;top:776px">
  <div class="brand brand-sm"><span class="mark"></span>Hartwig Akademie</div>
  <h2 class="abs h-display" style="left:39px;top:62px;font-size:21px;line-height:1.25">Journey from <span class="accent">Core</span><br><span class="accent">Skills to</span> Leadership</h2>
  <p class="abs body-xs" style="left:39px;top:137px;width:225px">Strong leaders grow from a solid base of core skills. This page shows the path from self management and clear communication to guiding others, building trust and shaping a team culture in which people learn together.</p>
  <p class="abs body-xs" style="left:39px;top:204px;width:225px">Use this second paragraph to add an example from practice, a short case or a question the group can discuss before moving on to the next step of the journey.</p>
  <div class="photo cool" role="img" aria-label="Photo of colleagues working at computers with headsets" style="left:307px;top:59px;width:257px;height:119px"></div>
  <div class="photo warm" role="img" aria-label="Photo of two colleagues discussing at a laptop" style="left:307px;top:185px;width:257px;height:119px"></div>
  <span class="pageno">5</span>
</section>

<section class="slide text-only" style="left:600px;top:776px">
  <div class="brand brand-sm"><span class="mark"></span>Hartwig Akademie</div>
  <h2 class="abs h-display" style="left:30px;top:26px;font-size:20px">Text Slide</h2>
  <p class="abs body-xs" style="left:30px;top:80px;width:540px;font-size:5.8px;line-height:11.5px">This layout holds longer text for handouts or detailed notes. Keep sentences short and clear so that the group can follow while you speak. Each block can cover one idea, one example or one task, and leaves enough white space around it to stay easy to read on screen and in print.</p>
  <p class="abs body-xs" style="left:30px;top:137px;width:540px;font-size:5.8px;line-height:11.5px">Add background on the topic here, such as a short model, a definition or the reason why this skill matters for leaders and teams. A calm structure with clear paragraphs helps participants find their way through the content and return to it later after the workshop has ended.</p>
  <p class="abs body-xs" style="left:30px;top:194px;width:540px;font-size:5.8px;line-height:11.5px">Use this part for an example from practice. Describe the situation, the challenge and what the team did next. Short real cases make new ideas easier to remember and invite the group to share their own experience in a guided discussion.</p>
  <p class="abs body-xs" style="left:30px;top:251px;width:540px;font-size:5.8px;line-height:11.5px">Close the slide with a short summary or a question for reflection. Ask what each person wants to try in the coming weeks and how they will notice progress, so that learning turns into action at the workplace.</p>
  <span class="pageno">6</span>
</section>

<section class="slide two-column" style="left:0;top:1154px">
  <div class="brand brand-sm"><span class="mark"></span>Hartwig Akademie</div>
  <h2 class="abs h-display" style="left:30px;top:26px;font-size:20px">Two column Text</h2>
  <div class="abs" style="left:30px;top:82px;width:256px">
    <p class="body-xs" style="font-size:5.8px;line-height:11.5px;margin-bottom:11px">The left column opens the topic. Describe the idea in simple words and name the main goal of this part of the training so that everyone starts from the same point.</p>
    <p class="body-xs" style="font-size:5.8px;line-height:11.5px;margin-bottom:11px">Then add more detail on the model or method, with a short example from the daily work of teams and leaders. Keep each paragraph focused on one thought, so the text stays light and easy to scan on screen and when printed for the group.</p>
    <p class="body-xs" style="font-size:5.8px;line-height:11.5px">End with a short note on what to keep in mind when applying it.</p>
  </div>
  <div class="abs" style="left:308px;top:82px;width:256px">
    <p class="body-xs" style="font-size:5.8px;line-height:11.5px;margin-bottom:11px">The right column can compare, contrast or extend the first. Place a second view here, such as the view of the team instead of the leader.</p>
    <p class="body-xs" style="font-size:5.8px;line-height:11.5px;margin-bottom:11px">Add a few practical steps, a list of questions or tips for the next meeting. This balance of two columns works well for pros and cons, before and after, or theory and practice in one clear view for all participants of the session.</p>
    <p class="body-xs" style="font-size:5.8px;line-height:11.5px">Finish with one key takeaway that links both sides together.</p>
  </div>
  <span class="pageno">7</span>
</section>

<section class="slide onboarding" style="left:600px;top:1154px">
  <div class="brand brand-sm"><span class="mark"></span>Hartwig Akademie</div>
  <h2 class="abs h-display" style="left:30px;top:26px;font-size:20px;line-height:1.2">Employee Onboarding<br>Guide Step</h2>
  <svg class="abs" style="left:53px;top:115px" width="500" height="66" viewBox="0 0 500 66">
    <g fill="#1f5b95">
      <polygon points="0,0 86,0 108,33 86,66 0,66 22,33"/>
      <polygon points="98,0 184,0 206,33 184,66 98,66 120,33"/>
      <polygon points="196,0 282,0 304,33 282,66 196,66 218,33"/>
      <polygon points="294,0 380,0 402,33 380,66 294,66 316,33"/>
      <polygon points="392,0 478,0 500,33 478,66 392,66 414,33"/>
    </g>
    <g fill="#fff" font-family="Roboto,sans-serif" font-size="14" text-anchor="middle">
      <text x="56" y="38">01</text><text x="154" y="38">02</text><text x="252" y="38">03</text><text x="350" y="38">04</text><text x="448" y="38">05</text>
    </g>
  </svg>
  <div class="step-dot" style="left:106px;top:222px"></div>
  <div class="step-dot" style="left:204px;top:222px"></div>
  <div class="step-dot" style="left:302px;top:222px"></div>
  <div class="step-dot" style="left:400px;top:222px"></div>
  <div class="step-dot" style="left:498px;top:222px"></div>
  <div class="step-label" style="left:69px;top:237px">Step 1</div>
  <div class="step-label" style="left:167px;top:237px">Step 2</div>
  <div class="step-label" style="left:265px;top:237px">Step 3</div>
  <div class="step-label" style="left:363px;top:237px">Step 4</div>
  <div class="step-label" style="left:461px;top:237px">Step 5</div>
  <span class="pageno">8</span>
</section>

<section class="slide model-6w" style="left:0;top:1532px">
  <div class="brand brand-sm"><span class="mark"></span>Hartwig Akademie</div>
  <svg class="abs" style="left:0;top:0" width="290" height="338" viewBox="0 0 290 338" font-family="Roboto,sans-serif">
    <circle cx="153" cy="167" r="112" fill="#e6ebf1"/>
    <g stroke="#fff" stroke-width="4">
      <line x1="153" y1="55" x2="153" y2="127"/><line x1="153" y1="207" x2="153" y2="279"/>
      <line x1="56" y1="111" x2="118" y2="147"/><line x1="188" y1="187" x2="250" y2="223"/>
      <line x1="56" y1="223" x2="118" y2="187"/><line x1="188" y1="147" x2="250" y2="111"/>
    </g>
    <circle cx="153" cy="167" r="40" fill="#fff" stroke="#1f5b95" stroke-width="3"/>
    <circle cx="153" cy="167" r="26" fill="#1f5b95"/>
    <text x="153" y="170" fill="#fff" font-size="7" font-weight="700" text-anchor="middle">6W</text>
    <g fill="#1f5b95">
      <circle cx="150" cy="97" r="6"/><circle cx="213" cy="130" r="6"/><circle cx="212" cy="205" r="6"/>
      <circle cx="150" cy="238" r="6"/><circle cx="77" cy="203" r="6"/><circle cx="77" cy="131" r="6"/>
    </g>
    <g font-size="6" fill="#111">
      <text x="78" y="83" font-weight="700">Who?</text>
      <text x="78" y="92">Who are the current</text><text x="78" y="99">and potential</text><text x="78" y="106">customers?</text>
      <text x="161" y="75" font-weight="700">What?</text>
      <text x="161" y="84">What do current and</text><text x="161" y="91">potential customers</text><text x="161" y="98">do with the product?</text>
      <text x="205" y="163" font-weight="700">Where?</text>
      <text x="205" y="172">Where do current</text><text x="205" y="179">customers buy the</text><text x="205" y="186">product?</text>
      <text x="166" y="251" font-weight="700">When?</text>
      <text x="166" y="260">When do current</text><text x="166" y="267">customers buy the</text><text x="166" y="274">product?</text>
      <text x="79" y="232" font-weight="700">Why?</text>
      <text x="79" y="241">Why do people buy</text><text x="79" y="248">from the company?</text>
      <text x="36" y="171" font-weight="700">Why Not?</text>
      <text x="36" y="180">Why don't people buy</text><text x="36" y="187">from the company?</text>
    </g>
  </svg>
  <h2 class="abs h-display" style="left:298px;top:86px;font-size:21px;line-height:1.25">6W Methodology of<br>Customer Analysis</h2>
  <p class="abs body-xs" style="left:298px;top:160px;width:240px;font-size:5.8px">Customer analysis looks at the current and future customers of an organization. The 6W analysis uses six simple questions to find out why people buy, when they buy and what they expect. Teams can use these answers to plan new offers, adjust their message and spot chances and risks early. It helps everyone look at the work from the view of the customer.</p>
  <span class="pageno">9</span>
</section>

<section class="slide model-triangle" style="left:600px;top:1532px">
  <div class="brand brand-sm"><span class="mark"></span>Hartwig Akademie</div>
  <svg class="abs" style="left:0;top:0" width="300" height="338" viewBox="0 0 300 338" font-family="Roboto,sans-serif">
    <circle cx="104" cy="129" r="68" fill="#8ea9c7" fill-opacity=".75"/>
    <circle cx="195" cy="121" r="73" fill="#1f5b95" fill-opacity=".75"/>
    <circle cx="151" cy="211" r="65" fill="#c9d6e5" fill-opacity=".85" stroke="#8ea9c7"/>
    <g stroke="#fff" stroke-width="1" fill="none">
      <polygon points="151,75 212,120 140,170"/>
      <line x1="151" y1="75" x2="151" y2="238"/>
    </g>
    <g stroke="#fff" stroke-width="1" stroke-dasharray="3 2" fill="none">
      <line x1="36" y1="157" x2="140" y2="170"/><line x1="250" y1="157" x2="212" y2="120"/>
    </g>
    <g font-size="5" fill="#fff" text-anchor="middle">
      <rect x="127" y="58" width="48" height="9" rx="4.5" fill="#8ea9c7"/><text x="151" y="64.5">Implementer</text>
      <rect x="85" y="87" width="40" height="9" rx="4.5" fill="#8ea9c7"/><text x="105" y="93.5">Completer</text>
      <rect x="162" y="89" width="42" height="9" rx="4.5" fill="#1f5b95"/><text x="183" y="95.5">Team Worker</text>
      <text x="72" y="110">Task</text><text x="231" y="110">People</text>
      <rect x="104" y="105" width="38" height="9" rx="4.5" fill="#8ea9c7"/><text x="123" y="111.5">Shaper</text>
      <rect x="126" y="130" width="46" height="9" rx="4.5" fill="#fff"/><text x="149" y="136.5" fill="#1f5b95">Coordinator</text>
      <rect x="14" y="153" width="50" height="9" rx="4.5" fill="#8ea9c7"/><text x="39" y="159.5">Monitor Evaluator</text>
      <rect x="222" y="153" width="66" height="9" rx="4.5" fill="#1f5b95"/><text x="255" y="159.5">Resource Investigator</text>
      <text x="151" y="223" fill="#8ea9c7">Think</text>
      <rect x="131" y="238" width="40" height="9" rx="4.5" fill="#8ea9c7"/><text x="151" y="244.5">Plant</text>
    </g>
  </svg>
  <h2 class="abs h-display" style="left:316px;top:104px;font-size:21px;line-height:1.25">Team Roles<br>Triangle</h2>
  <p class="abs body-xs" style="left:316px;top:178px;width:240px;font-size:5.6px;line-height:9px">This is a key part of team building. It looks at the roles people take in a team, how they focus on task, people or thinking, and how the mix of strengths helps the whole team to perform well.</p>
  <span class="pageno">10</span>
</section>

<section class="slide management" style="left:0;top:1910px">
  <div class="brand brand-sm"><span class="mark"></span>Hartwig Akademie</div>
  <div class="card-blue" style="left:19px;top:49px;width:136px;height:145px;padding:16px 12px">
    <svg class="icon-box" viewBox="0 0 22 22" fill="none" stroke="#fff" stroke-width="1.5"><path d="M2 18l6-6 4 4 8-9"/><path d="M15 7h5v5"/></svg>
    <p class="card-title" style="margin-top:36px">Foundational Business<br>Acumen</p>
    <p class="card-text">Short text about this topic in two lines.</p>
  </div>
  <div class="photo warm" role="img" aria-label="Photo of a smiling woman working on a laptop" style="left:19px;top:199px;width:136px;height:117px"></div>
  <div class="photo" role="img" aria-label="Photo of a man working at a laptop in an office" style="left:160px;top:49px;width:280px;height:267px"></div>
  <div class="abs" style="left:160px;top:49px;width:280px;height:97px;background:rgba(142,169,199,.55)"></div>
  <h2 class="abs h-display white" style="left:184px;top:68px;font-size:21px">About Management</h2>
  <p class="abs" style="left:184px;top:100px;width:240px;font-size:5.6px;line-height:9px;color:rgba(255,255,255,.85)">Good management connects goals, people and daily work. This page gives a short view of the role, the main tasks and what makes teams succeed.</p>
  <div class="abs" style="left:444px;top:49px;width:136px;height:145px;background:var(--blue-soft);padding:10px 12px;color:var(--white)">
    <p style="font-size:6px">Client satisfied</p>
    <div class="abs" style="right:12px;top:12px;width:24px;height:18px;border:2px solid rgba(255,255,255,.5);border-radius:2px"></div>
    <p class="abs h-display" style="left:12px;top:100px;font-size:30px">98%</p>
  </div>
  <div class="card-blue" style="left:444px;top:199px;width:136px;height:117px">
    <svg class="icon-box" viewBox="0 0 22 22" fill="none" stroke="#fff" stroke-width="1.5"><circle cx="11" cy="8" r="4"/><path d="M3 20c0-4 3.5-6 8-6s8 2 8 6"/></svg>
    <p class="card-title">Business Acumen</p>
    <p class="card-text">Short text about this topic in three lines for the group.</p>
  </div>
</section>

<section class="slide skills-gap" style="left:600px;top:1910px">
  <div class="brand brand-sm"><span class="mark"></span>Hartwig Akademie</div>
  <p class="abs body-xs" style="left:30px;top:58px;width:200px;font-size:5.6px;line-height:9px">Skills change fast in most roles. This slide shows where gaps appear and why steady learning helps people and teams keep up with new tasks.</p>
  <h2 class="abs h-display" style="left:305px;top:55px;font-size:21px;line-height:1.25">Skills Gap <span class="accent">Need for</span><br><span class="accent">Continuous</span> Learning</h2>
  <div class="photo warm" role="img" aria-label="Photo of colleagues shaking hands across a desk" style="left:0;top:139px;width:600px;height:199px"></div>
  <div class="card-blue" style="left:22px;top:174px;width:136px;height:123px;background:rgba(142,169,199,.92)">
    <svg class="icon-box" viewBox="0 0 22 22" fill="none" stroke="#fff" stroke-width="1.5"><circle cx="11" cy="8" r="4"/><path d="M3 20c0-4 3.5-6 8-6s8 2 8 6"/></svg>
    <p class="card-title" style="margin-top:18px">Business Acumen</p><p class="card-text">Short text about this skill area in two lines.</p>
  </div>
  <div class="card-blue" style="left:161px;top:174px;width:136px;height:123px">
    <svg class="icon-box" viewBox="0 0 22 22" fill="none" stroke="#fff" stroke-width="1.5"><circle cx="11" cy="8" r="4"/><path d="M3 20c0-4 3.5-6 8-6s8 2 8 6"/></svg>
    <p class="card-title" style="margin-top:18px">Business Acumen</p><p class="card-text">Short text about this skill area in two lines.</p>
  </div>
  <div class="card-blue" style="left:300px;top:174px;width:136px;height:123px">
    <svg class="icon-box" viewBox="0 0 22 22" fill="none" stroke="#fff" stroke-width="1.5"><circle cx="11" cy="8" r="4"/><path d="M3 20c0-4 3.5-6 8-6s8 2 8 6"/></svg>
    <p class="card-title" style="margin-top:18px">Business Acumen</p><p class="card-text">Short text about this skill area in two lines.</p>
  </div>
  <div class="card-blue" style="left:440px;top:174px;width:136px;height:123px">
    <svg class="icon-box" viewBox="0 0 22 22" fill="none" stroke="#fff" stroke-width="1.5"><circle cx="11" cy="8" r="4"/><path d="M3 20c0-4 3.5-6 8-6s8 2 8 6"/></svg>
    <p class="card-title" style="margin-top:18px">Business Acumen</p><p class="card-text">Short text about this skill area in two lines.</p>
  </div>
</section>

<section class="slide chart" style="left:0;top:2288px">
  <div class="brand brand-sm"><span class="mark"></span>Hartwig Akademie</div>
  <h2 class="abs h-display" style="left:30px;top:24px;font-size:20px">Our Expert <span class="accent">Chart Slide</span></h2>
  <svg class="abs" style="left:29px;top:80px" width="190" height="220" viewBox="0 0 190 220" font-family="Roboto,sans-serif">
    <g font-size="4.5" fill="#8a929c" text-anchor="end">
      <text x="10" y="192">0</text><text x="10" y="172">50</text><text x="10" y="152">100</text><text x="10" y="132">150</text><text x="10" y="112">200</text>
      <text x="10" y="92">250</text><text x="10" y="72">300</text><text x="10" y="52">350</text><text x="10" y="32">400</text><text x="10" y="12">450</text>
    </g>
    <g stroke="#e3e7ec" stroke-width=".6">
      <line x1="14" y1="190" x2="188" y2="190"/><line x1="14" y1="150" x2="188" y2="150"/><line x1="14" y1="110" x2="188" y2="110"/><line x1="14" y1="70" x2="188" y2="70"/><line x1="14" y1="30" x2="188" y2="30"/>
    </g>
    <g>
      <rect x="22" y="110" width="5" height="80" fill="#8ea9c7"/><rect x="28" y="40" width="5" height="150" fill="#1f5b95"/><rect x="34" y="110" width="5" height="80" fill="#c9d6e5"/>
      <rect x="62" y="35" width="5" height="155" fill="#1f5b95"/><rect x="68" y="110" width="5" height="80" fill="#8ea9c7"/><rect x="74" y="110" width="5" height="80" fill="#c9d6e5"/>
      <rect x="108" y="55" width="5" height="135" fill="#1f5b95"/><rect x="114" y="85" width="5" height="105" fill="#8ea9c7"/><rect x="120" y="115" width="5" height="75" fill="#c9d6e5"/>
      <rect x="150" y="40" width="5" height="150" fill="#1f5b95"/><rect x="156" y="115" width="5" height="75" fill="#8ea9c7"/><rect x="162" y="100" width="5" height="90" fill="#c9d6e5"/>
    </g>
    <g font-size="4.5" fill="#8a929c" text-anchor="middle">
      <text x="30" y="201">Group 1</text><text x="70" y="201">Group 2</text><text x="115" y="201">Group 3</text><text x="158" y="201">Group 4</text>
    </g>
  </svg>
  <div class="abs" style="left:236px;top:54px;width:175px;height:241px;background:var(--white);box-shadow:0 2px 10px rgba(0,0,0,.12)">
    <svg class="abs" style="left:38px;top:36px" width="100" height="100" viewBox="0 0 100 100">
      <circle cx="50" cy="50" r="44" fill="none" stroke="#e6ebf1" stroke-width="5"/>
      <circle cx="50" cy="50" r="44" fill="none" stroke="#1f5b95" stroke-width="5" stroke-dasharray="248.8 276.5" transform="rotate(-54 50 50)"/>
      <circle cx="50" cy="6" r="5" fill="#c9d6e5"/>
      <text x="50" y="56" text-anchor="middle" font-family="Roboto Condensed,sans-serif" font-size="18" fill="#5b6470">90%</text>
    </svg>
    <p class="abs" style="left:0;top:156px;width:175px;text-align:center;font-size:7px;color:var(--text)">Number 01</p>
    <p class="abs body-xs" style="left:30px;top:186px;width:115px;text-align:center;font-size:5.6px;line-height:9px">Short note on what this value shows and why it matters.</p>
  </div>
  <div class="abs" style="left:435px;top:75px;width:135px">
    <p class="body-xs" style="font-size:5.6px;line-height:9px;margin-bottom:7px">Explain the first finding from the chart and what it means for the group.</p>
    <p class="body-xs" style="font-size:5.6px;line-height:9px;margin-bottom:7px">Add a second point that compares the groups and names the clear trend.</p>
    <p class="body-xs" style="font-size:5.6px;line-height:9px">Close with one idea on how the team can use these results next.</p>
  </div>
  <span class="pageno">13</span>
</section>

<section class="slide quote" style="left:600px;top:2288px">
  <div class="brand brand-sm"><span class="mark"></span>Hartwig Akademie</div>
  <div class="abs" style="left:0;top:0;width:208px;height:338px;background:var(--blue)"></div>
  <div class="photo cool" role="img" aria-label="Large quotation mark filled with photos of smiling participants" style="left:20px;top:102px;width:186px;height:142px;border-radius:60px 60px 60px 10px"></div>
  <h2 class="abs h-display" style="left:254px;top:118px;font-size:19.5px;line-height:1.3">Participant Journey The<br>Learning <span class="accent">Experience</span><br><span class="accent">from Enrollment to</span><br>Certification</h2>
  <div class="abs" style="left:254px;top:266px;width:110px;height:1px;background:var(--blue-pale)"></div>
  <div class="abs" style="left:254px;top:265px;width:38px;height:2px;background:var(--blue-soft)"></div>
  <p class="abs sub" style="left:384px;top:260px;font-size:10px;color:var(--text);font-weight:400">Quotes – By Ceo</p>
  <span class="pageno">14</span>
</section>

<section class="slide website" style="left:0;top:2666px">
  <div class="brand brand-sm"><span class="mark"></span>Hartwig Akademie</div>
  <div class="abs" style="left:0;top:53px;width:600px;height:148px;background:var(--blue)"></div>
  <h2 class="abs h-display white" style="left:0;top:72px;width:600px;text-align:center;font-size:20px">Website Mockup</h2>
  <div class="abs" style="left:47px;top:128px;width:505px;height:176px;background:var(--grey-pale)"></div>
  <div class="abs" style="left:156px;top:109px;width:288px;height:195px;background:var(--white);box-shadow:0 2px 8px rgba(0,0,0,.15)">
    <div style="height:20px;background:#eceff2;border-bottom:1px solid #dde1e6;display:flex;align-items:center;padding-left:6px;gap:3px">
      <span style="width:4px;height:4px;border-radius:50%;background:#e5665c"></span><span style="width:4px;height:4px;border-radius:50%;background:#f0bf4c"></span><span style="width:4px;height:4px;border-radius:50%;background:#62c554"></span>
      <span style="margin-left:6px;width:200px;height:8px;background:#fff;border-radius:2px;font-size:4px;color:#888;padding-left:4px;line-height:8px">www.hartwig-akademie.de</span>
    </div>
    <div class="brand" style="left:30px;top:38px;font-size:10px"><span class="mark" style="width:7px;height:7px"></span>Hartwig Akademie</div>
    <p class="abs" style="left:30px;top:62px;font-size:6px;font-weight:700;color:#333">Trainings, Workshops, Beratung und Coachings</p>
    <div class="abs" style="left:30px;top:74px;width:150px;height:3px;background:#d8dde3"></div>
    <div class="abs" style="left:30px;top:80px;width:130px;height:3px;background:#d8dde3"></div>
    <div class="abs" style="left:55px;top:92px;width:110px;height:12px;border:1px solid #c9d0d8;border-radius:6px"></div>
    <div class="abs" style="left:30px;top:118px;width:40px;height:3px;background:#b8c1cc"></div>
    <div class="abs" style="left:30px;top:126px;width:140px;height:2px;background:#dde2e7"></div>
    <div class="abs" style="left:30px;top:131px;width:150px;height:2px;background:#dde2e7"></div>
    <div class="abs" style="left:30px;top:136px;width:130px;height:2px;background:#dde2e7"></div>
    <div class="abs" style="left:30px;top:146px;width:160px;height:2px;background:#9fb3cc"></div>
    <div class="abs" style="left:30px;top:151px;width:150px;height:2px;background:#9fb3cc"></div>
    <div class="abs" style="left:30px;top:156px;width:155px;height:2px;background:#9fb3cc"></div>
    <div class="abs" style="left:30px;top:161px;width:140px;height:2px;background:#9fb3cc"></div>
    <div class="photo cool" role="img" aria-label="Small portrait photo of the trainer" style="left:220px;top:60px;width:34px;height:34px;border-radius:50%"></div>
    <div class="abs" style="left:210px;top:102px;width:50px;height:2px;background:#dde2e7"></div>
    <div class="abs" style="left:210px;top:107px;width:40px;height:2px;background:#dde2e7"></div>
    <div class="abs" style="left:60px;top:174px;width:115px;height:16px;background:var(--blue-soft);border-radius:8px;font-size:5.5px;color:#fff;text-align:center;line-height:16px">www.hartwig-akademie.de</div>
    <svg class="abs" style="left:180px;top:175px" width="14" height="14" viewBox="0 0 14 14" fill="none" stroke="#5b6470" stroke-width="1.4"><circle cx="6" cy="6" r="4"/><path d="M9 9l4 4"/></svg>
  </div>
  <span class="pageno">15</span>
</section>

<section class="slide closing" style="left:600px;top:2666px">
  <div class="abs" style="left:0;top:0;width:416px;height:183px;background:var(--blue)"></div>
  <div class="photo cool" role="img" aria-label="Portrait photo of the trainer" style="left:416px;top:0;width:184px;height:188px"></div>
  <h1 class="abs h-display white" style="left:30px;top:60px;font-size:44px">Thank you!</h1>
  <p class="abs name" style="left:30px;top:242px">Dr. phil. Lena Hartwig, MBA</p>
  <div class="badge" style="left:30px;top:259px">Expertin für Didaktik und Selbstführung</div>
  <div class="brand brand-lg" style="left:394px;top:246px"><span class="mark"></span>Hartwig Akademie</div>
</section>

</body>
</html>
```